Alaskan medical billing service needs a business card design

We need a business card design for a medical billing service, located in Anchorage, AK. We provide medical claims billing and management to Alaskan medical practices/clinics. We would like to see designs that depict Alaskan Mountain Ranges, or water features, or trees. An outdoorsy feel, perhaps. Not exactly sure.

```html
<!DOCTYPE html>
<html lang="en">
<head>
<meta charset="utf-8">
<title>Tundra Ridge Billing — Business Card</title>
<link rel="stylesheet" href="https://fonts.googleapis.com/css2?family=Open+Sans:wght@400;600;700&display=swap">
<style>
  :root {
    --card-bg: #ffffff;
    --brand-blue: #0f8fcb;
    --brand-green: #8dc63f;
    --text-grey: #595959;
    --name-grey: #666666;
  }
  html, body {
    margin: 0;
    padding: 0;
    width: 1200px;
    height: 720px;
    overflow: hidden;
    background: var(--card-bg);
  }
  .card {
    position: relative;
    width: 1200px;
    height: 720px;
    background: var(--card-bg);
    font-family: "Open Sans", Arial, sans-serif;
    overflow: hidden;
  }
  .waves {
    position: absolute;
    inset: 0;
    width: 1200px;
    height: 720px;
  }
  .wave-blue { fill: var(--brand-blue); }
  .wave-green { fill: var(--brand-green); }

  .holder {
    position: absolute;
    top: 78px;
    right: 88px;
    text-align: center;
    color: var(--name-grey);
  }
  .holder-name {
    margin: 0;
    font-size: 32px;
    font-weight: 700;
    line-height: 1.15;
  }
  .holder-title {
    margin: 0;
    font-size: 30px;
    font-weight: 400;
    line-height: 1.15;
  }

  .brand {
    position: absolute;
    left: 96px;
    top: 200px;
    width: 535px;
    text-align: center;
  }
  .brand-mark {
    display: block;
    width: 140px;
    height: 140px;
    margin: 0 auto 34px;
    border-radius: 50%;
    background: var(--brand-green);
  }
  .brand-name {
    margin: 0;
    font-size: 34px;
    font-weight: 600;
    letter-spacing: 1px;
    color: var(--brand-blue);
    line-height: 1.2;
  }

  .contact {
    position: absolute;
    left: 684px;
    top: 272px;
    margin: 0;
    padding: 0;
    list-style: none;
    color: var(--text-grey);
    font-size: 32px;
    line-height: 1.08;
  }
  .contact-item {
    display: flex;
    align-items: flex-start;
    margin-bottom: 34px;
  }
  .contact-icon {
    width: 48px;
    height: 40px;
    margin-right: 24px;
    flex: none;
    fill: var(--brand-blue);
  }
  .contact-item--address .contact-icon { margin-top: 4px; }
</style>
</head>
<body>
<div class="card">
  <svg class="waves" viewBox="0 0 1200 720" aria-hidden="true">
    <path class="wave-blue" d="M40,508 C280,472 560,520 860,500 C560,548 280,500 40,530 Z"/>
    <path class="wave-green" d="M40,542 C360,500 720,590 1160,522 L1160,548 C720,612 360,528 40,568 Z"/>
    <path class="wave-blue" d="M40,598 C420,572 800,642 1160,588 L1160,675 L40,675 Z"/>
  </svg>

  <div class="holder">
    <p class="holder-name">Marla J. Henning</p>
    <p class="holder-title">Owner</p>
  </div>

  <div class="brand">
    <span class="brand-mark"></span>
    <p class="brand-name">TUNDRA RIDGE BILLING, LLC</p>
  </div>

  <ul class="contact">
    <li class="contact-item contact-item--address">
      <svg class="contact-icon" viewBox="0 0 48 40" aria-hidden="true">
        <path d="M24,2 L2,22 L8,22 L8,38 L19,38 L19,27 L29,27 L29,38 L40,38 L40,22 L46,22 Z"/>
      </svg>
      <span>PO Box 204588<br>Anchorage, AK 99507</span>
    </li>
    <li class="contact-item">
      <svg class="contact-icon" viewBox="0 0 48 40" aria-hidden="true">
        <path d="M14,3 L20,3 L22,11 L18,14 C19,21 21,26 25,31 L29,29 L33,35 L29,38 C20,37 13,22 14,3 Z"/>
      </svg>
      <span>907-555-0142</span>
    </li>
    <li class="contact-item">
      <svg class="contact-icon" viewBox="0 0 48 40" aria-hidden="true">
        <path d="M14,2 L30,2 L34,6 L34,16 L14,16 Z M10,18 L38,18 L38,38 L10,38 Z M15,24 L33,24 L33,27 L15,27 Z M15,30 L33,30 L33,33 L15,33 Z" fill-rule="evenodd"/>
      </svg>
      <span>907-555-0143</span>
    </li>
  </ul>
</div>
</body>
</html>
```